Estate Agent/Real Estate valuation tool

We need a design for our our new estate agent valuation tool.

The tool allows users to book a valuation of their house/property with the estate agent, after they choose there property they can then complete their details and choose a booking time.

The mock up of the design we want is attached to this project.(Main Screen)

This also needs to be responsive so the design is easy to use on a mobile device.

Target Market(s)

estate agents

Industry/Entity Type

Real Estate Agent

Number of Pages Required

1 page

Requirements
Must have
• Section 2 and 3 greyed out when user is on step 1
• Section 1 and 3 greyed out when user is on step 2
• Section 1 and 2 greyed out when the user is on step 3
• *** Design must be shown for mobile/ipad and desktop
Nice to have
• Clean and Simple
Should not have
• Dark colours

```html
<!DOCTYPE html>
<html lang="en">
<head>
<meta charset="utf-8">
<title>Book Your Valuation Online</title>
<link rel="stylesheet" href="https://fonts.googleapis.com/css2?family=Montserrat:wght@400;500;600;700&display=swap">
<style>
  :root {
    --green: #3dba78;
    --green-body: #84cb9d;
    --mint-head: #a0dcbc;
    --mint-body: #c2e5d1;
    --mint-tab: #7fd0a4;
    --white: #ffffff;
    --field-label: #999999;
    --label-dark: #2b2b2b;
    --slot-text: #7a7a7a;
    --slot-time-bg: #f0f0f0;
    --button-grey: #e5e5e5;
    --logo-grey: #d8d8d8;
  }
  * { box-sizing: border-box; margin: 0; padding: 0; }
  html, body { width: 1200px; height: 750px; overflow: hidden; background: var(--white); }
  body { font-family: "Montserrat", Arial, sans-serif; position: relative; }

  .brand-mark {
    position: absolute; left: 536px; top: 23px; width: 127px; height: 127px;
    background: var(--logo-grey);
  }
  .page-title {
    position: absolute; left: 0; right: 0; top: 163px; text-align: center;
    color: var(--green); font-size: 43px; font-weight: 700; letter-spacing: 0.3px;
  }

  .steps { position: absolute; left: 85px; top: 234px; display: flex; gap: 28px; }
  .step { position: relative; width: 324px; height: 478px; background: var(--mint-body); }
  .step--active { background: var(--green-body); }

  .step__header {
    height: 75px; display: flex; align-items: center; justify-content: center; gap: 10px;
    background: var(--mint-head); color: var(--white); font-size: 22px; font-weight: 700;
  }
  .step--active .step__header { background: var(--green); }
  .step__number {
    width: 28px; height: 28px; border-radius: 50%; background: var(--white);
    color: var(--mint-head); font-size: 18px; font-weight: 700;
    display: flex; align-items: center; justify-content: center;
  }
  .step--active .step__number { color: var(--green); }

  .step__footer {
    position: absolute; left: 0; right: 0; bottom: 0; height: 75px;
    display: flex; align-items: center; justify-content: center;
    background: var(--mint-head); color: var(--white); font-size: 25px; font-weight: 700; letter-spacing: 0.3px;
  }
  .step--active .step__footer { background: var(--green); }

  .field-label {
    position: absolute; left: 20px; font-size: 18px; font-weight: 400; color: var(--field-label);
    line-height: 20px;
  }
  .step--active .field-label { color: var(--label-dark); font-weight: 500; }
  .field {
    position: absolute; left: 19px; width: 287px; height: 40px; background: var(--white);
    font-size: 18px; color: #a8a8a8; padding-left: 11px; display: flex; align-items: center;
  }
  .search-button {
    position: absolute; right: 0; top: 0; width: 82px; height: 40px; background: var(--button-grey);
    color: var(--label-dark); font-size: 14px; font-weight: 600; letter-spacing: 0.3px;
    display: flex; align-items: center; justify-content: center;
  }

  .day-tabs { position: absolute; left: 19px; top: 95px; width: 287px; display: flex; justify-content: space-between; }
  .day-tab {
    width: 42px; height: 42px; background: var(--white); color: var(--slot-text);
    font-size: 11px; font-weight: 600; line-height: 12px; text-align: center;
    display: flex; flex-direction: column; align-items: center; justify-content: center;
  }
  .day-tab sup { font-size: 7px; line-height: 0; }
  .day-tab--selected { background: var(--mint-tab); color: var(--white); font-size: 7px; }

  .slots { position: absolute; left: 19px; top: 149px; width: 287px; display: flex; flex-direction: column; gap: 10px; }
  .slot { display: flex; height: 40px; font-size: 14px; font-weight: 600; color: var(--slot-text); }
  .slot__date { flex: 1; background: var(--white); display: flex; align-items: center; padding-left: 13px; }
  .slot__time { width: 82px; background: var(--slot-time-bg); display: flex; align-items: center; justify-content: center; }
</style>
</head>
<body>
  <div class="brand-mark"></div>
  <h1 class="page-title">Book Your Valuation Online</h1>

  <main class="steps">
    <section class="step step--active">
      <header class="step__header"><span class="step__number">1</span>Property Details</header>
      <span class="field-label" style="top:91px">Postcode</span>
      <div class="field" style="top:119px"><span class="search-button">SEARCH</span></div>
      <div class="field" style="top:206px">Street</div>
      <div class="field" style="top:256px">City</div>
      <div class="field" style="top:306px">County</div>
      <footer class="step__footer">PROCEED</footer>
    </section>

    <section class="step">
      <header class="step__header"><span class="step__number">2</span>Your Details</header>
      <span class="field-label" style="top:91px">Your Name</span>
      <div class="field" style="top:119px"></div>
      <span class="field-label" style="top:179px">Your Email</span>
      <div class="field" style="top:207px"></div>
      <span class="field-label" style="top:267px">Your Contact Number</span>
      <div class="field" style="top:295px"></div>
      <footer class="step__footer">PROCEED</footer>
    </section>

    <section class="step">
      <header class="step__header"><span class="step__number">3</span>Appointment Time</header>
      <div class="day-tabs">
        <div class="day-tab">Today</div>
        <div class="day-tab day-tab--selected">Tomorrow</div>
        <div class="day-tab">Mon<span>30<sup>th</sup></span></div>
        <div class="day-tab">Tue<span>1<sup>st</sup></span></div>
        <div class="day-tab">Wed<span>2<sup>nd</sup></span></div>
        <div class="day-tab">Thu<span>3<sup>rd</sup></span></div>
      </div>
      <div class="slots">
        <div class="slot"><span class="slot__date">Sunday 29th November</span><span class="slot__time">08:30</span></div>
        <div class="slot"><span class="slot__date">Sunday 29th November</span><span class="slot__time">10:30</span></div>
        <div class="slot"><span class="slot__date">Sunday 29th November</span><span class="slot__time">12:30</span></div>
        <div class="slot"><span class="slot__date">Sunday 29th November</span><span class="slot__time">14:30</span></div>
        <div class="slot"><span class="slot__date">Sunday 29th November</span><span class="slot__time">16:30</span></div>
      </div>
      <footer class="step__footer">CONFIRM BOOKING</footer>
    </section>
  </main>
</body>
</html>
```